" A empresa presta serviço de desenvolvimento de softwares, aplicativos e sistemas, visando o mercado norte-americano, mais especificamente o Vale do Silício. (pessoas físicas e jurídicas). "

```html
<!DOCTYPE html>
<html lang="pt-BR">
<head>
<meta charset="UTF-8">
<title>Nexo – Cartão de visita</title>
<link rel="stylesheet" href="https://fonts.googleapis.com/css2?family=Open+Sans:wght@400;600;700&display=swap">
<style>
  :root {
    --teal: #2bb3a1;
    --orange: #f6a623;
    --grey: #b9b9b9;
    --ink: #4a4a4a;
    --ink-soft: #7a7a7a;
    --card: #ffffff;
    --backdrop: #eceeef;
  }
  * { box-sizing: border-box; margin: 0; padding: 0; }
  html, body {
    width: 1200px; height: 1200px; overflow: hidden;
    background: var(--backdrop);
    font-family: "Open Sans", Arial, sans-serif;
  }
  .canvas { position: relative; width: 1200px; height: 1200px; }
  .card {
    position: absolute; left: 150px; width: 900px; height: 500px;
    background: var(--card);
    box-shadow: 0 6px 24px rgba(0,0,0,0.12);
    overflow: hidden;
  }
  .card--front { top: 70px; }
  .card--contact { top: 630px; }

  .brand-name {
    font-family: "Open Sans", Arial, sans-serif;
    font-weight: 600;
    color: var(--teal);
    letter-spacing: 2px;
    line-height: 1;
  }
  .card--front .brand-name {
    position: absolute; top: 170px; left: 0; width: 100%;
    text-align: center; font-size: 120px;
  }
  .card--contact .brand-name {
    position: absolute; top: 150px; left: 70px; font-size: 96px;
  }

  .band { position: absolute; left: 0; bottom: 0; width: 100%; height: 46px; }
  .band svg { position: absolute; inset: 0; width: 100%; height: 100%; }
  .band-url {
    position: absolute; bottom: 0; height: 46px; line-height: 46px;
    color: #fff; font-size: 17px; font-weight: 400; letter-spacing: 0.5px;
  }
  .card--front .band-url { left: 285px; }
  .card--contact .band-url { left: 150px; }

  .contact-block { position: absolute; left: 500px; top: 125px; color: var(--ink); }
  .person-name { font-size: 22px; font-weight: 700; line-height: 1.1; }
  .person-role { font-size: 17px; color: var(--ink-soft); margin-bottom: 22px; }
  .contact-list { list-style: none; }
  .contact-item {
    display: flex; align-items: flex-start; gap: 12px;
    font-size: 15px; line-height: 1.35; color: var(--ink-soft);
    margin-bottom: 10px;
  }
  .contact-item svg { flex: 0 0 16px; width: 16px; height: 16px; margin-top: 2px; fill: var(--teal); }
  .contact-item--email { margin-top: 14px; }
</style>
</head>
<body>
<main class="canvas">

  <section class="card card--front" aria-label="Frente do cartão">
    <div class="brand-name">Nexo</div>
    <div class="band">
      <svg viewBox="0 0 900 46" preserveAspectRatio="none" aria-hidden="true">
        <polygon points="0,0 270,0 250,46 0,46" fill="var(--grey)"/>
        <polygon points="270,0 900,0 900,46 250,46" fill="var(--teal)"/>
      </svg>
      <span class="band-url">www.nexo.com.br</span>
    </div>
  </section>

  <section class="card card--contact" aria-label="Verso do cartão">
    <div class="brand-name">Nexo</div>

    <div class="contact-block">
      <p class="person-name">Nome Sobrenome</p>
      <p class="person-role">Cargo</p>
      <ul class="contact-list">
        <li class="contact-item">
          <svg viewBox="0 0 16 16" aria-hidden="true"><rect x="4" y="1" width="8" height="14" rx="1.5"/><rect x="5.5" y="3" width="5" height="8" fill="#fff"/></svg>
          <span>+55 11 0000.0000</span>
        </li>
        <li class="contact-item">
          <svg viewBox="0 0 16 16" aria-hidden="true"><path d="M4 1.5l2.5 3-1.6 1.6c.9 2 2.5 3.6 4.5 4.5l1.6-1.6 3 2.5-1.5 2.5C7 13.5 2.5 9 1.5 3z"/></svg>
          <span>+55 11 0000.0000</span>
        </li>
        <li class="contact-item">
          <svg viewBox="0 0 16 16" aria-hidden="true"><path d="M8 1a5 5 0 0 0-5 5c0 3.8 5 9 5 9s5-5.2 5-9a5 5 0 0 0-5-5zm0 7a2 2 0 1 1 0-4 2 2 0 0 1 0 4z"/></svg>
          <span>Av. das Palmeiras, 940, cj 12<br>Vila Nova - São Paulo/SP</span>
        </li>
        <li class="contact-item contact-item--email">
          <svg viewBox="0 0 16 16" aria-hidden="true"><rect x="1" y="3" width="14" height="10" rx="1"/><path d="M1.5 4L8 9l6.5-5" fill="none" stroke="#fff" stroke-width="1.4"/></svg>
          <span>contato@nexo.com.br</span>
        </li>
      </ul>
    </div>

    <div class="band">
      <svg viewBox="0 0 900 46" preserveAspectRatio="none" aria-hidden="true">
        <polygon points="0,0 130,0 110,46 0,46" fill="var(--grey)"/>
        <polygon points="130,0 900,0 900,46 110,46" fill="var(--orange)"/>
      </svg>
      <span class="band-url">www.nexo.com.br</span>
    </div>
  </section>

</main>
</body>
</html>
```